high end contractor

high end contracting company we do all phases of construction kitchen,bathrooms,etc... please look at my website before you design www.harborkeybuild.com

would love some sort of lines or logo or both

Industry/Entity Type

Construction

Contact Information for Business Card

company name: oak & meridian contracting address: 318 fenwick st mount Vernon ny 10552 email: harborkeybuild@mailbrook.com website: www.harborkeybuild.com office#: 914-208-3916 fax#: 914-208-5523 dominic valtersen mobile# 917-526-0389

```html
<!DOCTYPE html>
<html lang="en">
<head>
<meta charset="utf-8">
<title>Oak &amp; Meridian Contracting – Business Card</title>
<link rel="stylesheet" href="https://fonts.googleapis.com/css2?family=Montserrat:wght@600&family=Roboto:ital,wght@0,400;1,300&display=swap">
<style>
  :root {
    --page-bg: #e4e4e4;
    --card-white: #ffffff;
    --mint: #5cfdb9;
    --mint-text: #4ee6ad;
    --mint-pale: #e0f6f2;
    --blue: #2a3cf2;
    --navy: #0e1160;
    --lavender: #c9c2f7;
    --ink-light: #ffffff;
  }
  * { box-sizing: border-box; margin: 0; padding: 0; }
  html, body { width: 1200px; height: 901px; overflow: hidden; }
  body {
    position: relative;
    background: var(--page-bg);
    font-family: "Roboto", Arial, sans-serif;
  }
  .card {
    position: absolute;
    left: 352px;
    width: 540px;
    height: 300px;
    background: var(--card-white);
    overflow: hidden;
  }
  .card--front { top: 89px; }
  .card--back { top: 449px; }

  .card-art { position: absolute; inset: 0; width: 540px; height: 300px; }

  /* front */
  .front-website {
    position: absolute;
    left: 20px;
    top: 264px;
    transform: rotate(-90deg);
    transform-origin: left top;
    color: var(--mint-text);
    font-size: 14px;
    letter-spacing: 3px;
    white-space: nowrap;
  }
  .front-brand {
    position: absolute;
    left: 0;
    right: 0;
    top: 84px;
    display: flex;
    flex-direction: column;
    align-items: center;
    gap: 10px;
  }
  .front-brand__dot {
    width: 40px; height: 40px;
    border-radius: 50%;
    border: 6px solid var(--ink-light);
  }
  .front-brand__name {
    color: var(--ink-light);
    font-family: "Montserrat", Arial, sans-serif;
    font-weight: 600;
    font-size: 21px;
    line-height: 1.15;
    text-align: center;
    text-transform: uppercase;
  }

  /* back */
  .back-brand {
    position: absolute;
    left: 24px;
    top: 24px;
    display: flex;
    align-items: center;
    gap: 9px;
  }
  .back-brand__dot {
    width: 38px; height: 38px;
    border-radius: 50%;
    border: 6px solid var(--mint-text);
  }
  .back-brand__name {
    color: var(--mint-text);
    font-family: "Montserrat", Arial, sans-serif;
    font-weight: 600;
    font-size: 14px;
    line-height: 1.1;
    text-transform: uppercase;
  }
  .name-bar {
    position: absolute;
    left: 0; top: 132px;
    width: 73px; height: 18px;
    background: var(--mint);
  }
  .person-name {
    position: absolute;
    left: 77px; top: 124px;
    color: var(--mint-text);
    font-style: italic;
    font-weight: 300;
    font-size: 24px;
    white-space: nowrap;
  }
  .person-role {
    position: absolute;
    left: 184px; top: 157px;
    color: var(--mint-text);
    font-size: 12px;
  }
  .contact-list {
    position: absolute;
    left: 14px; top: 207px;
    list-style: none;
    color: var(--ink-light);
    font-size: 13px;
    line-height: 22.3px;
    white-space: nowrap;
  }
  .contact-divider {
    position: absolute;
    left: 247px; top: 211px;
    width: 1px; height: 82px;
    background: rgba(255,255,255,0.8);
  }
  .contact-address {
    position: absolute;
    left: 258px; top: 230px;
    width: 185px;
    color: var(--ink-light);
    font-size: 13px;
    line-height: 22px;
  }
</style>
</head>
<body>

<section class="card card--front" aria-label="Business card front">
  <svg class="card-art" viewBox="0 0 540 300">
    <defs>
      <linearGradient id="front-art-fill" x1="0" y1="1" x2="1" y2="0">
        <stop offset="0" stop-color="#e9e6fb"/>
        <stop offset="0.3" stop-color="#9c8ff0"/>
        <stop offset="0.55" stop-color="#2a3cf2"/>
        <stop offset="1" stop-color="#0e1160"/>
      </linearGradient>
    </defs>
    <rect x="50" y="0" width="490" height="300" fill="url(#front-art-fill)"
          role="img" aria-label="Abstract geometric backdrop in blue, violet and teal"/>
  </svg>
  <div class="front-website">www.harborkeybuild.com</div>
  <div class="front-brand">
    <span class="front-brand__dot"></span>
    <div class="front-brand__name">Oak &amp; Meridian<br>Contracting</div>
  </div>
</section>

<section class="card card--back" aria-label="Business card back">
  <svg class="card-art" viewBox="0 0 540 300">
    <defs>
      <linearGradient id="back-art-fill" x1="0" y1="0" x2="1" y2="1">
        <stop offset="0" stop-color="#6b5ef0"/>
        <stop offset="0.5" stop-color="#2a3cf2"/>
        <stop offset="1" stop-color="#b4aaf5"/>
      </linearGradient>
    </defs>
    <polygon points="291,0 540,0 540,250" fill="var(--mint-pale)"/>
    <polygon points="413,0 540,0 540,300 451,300 451,230 480,150 413,60"
             fill="url(#back-art-fill)" role="img"
             aria-label="Abstract geometric accent in blue and violet"/>
    <polygon points="0,202 403,202 451,244 451,300 0,300" fill="var(--mint)"/>
  </svg>

  <div class="back-brand">
    <span class="back-brand__dot"></span>
    <div class="back-brand__name">Oak &amp; Meridian<br>Contracting</div>
  </div>

  <span class="name-bar"></span>
  <div class="person-name">Dominic Valtersen</div>
  <div class="person-role">Designation</div>

  <ul class="contact-list">
    <li>Office: 914-208-3916</li>
    <li>Mobile: 917-526-0389</li>
    <li>Fax: 914-208-5523</li>
    <li>email: harborkeybuild@mailbrook.com</li>
  </ul>
  <span class="contact-divider"></span>
  <p class="contact-address">Address: 318 fenwick st mount Vernon ny</p>
</section>

</body>
</html>
```